Holistic/ Sports Psychologist needs flyer design

I need a flyer designed that catches the attention of potential customers - (parents of young athletes and athletes) who may be looking for psychological services. I have a logo and all the relevant info for the flyer but would like someone to take it and make it look creative, fun, fresh and attention getting for high school and college athletes. The colors used can be from my logo design which represents my holistic approach.
Target Market(s)
high school and collegiate athletes
Industry/Entity Type
sports psychology
Requirements
Must have
- Info I put on the flyer with my logo and please add some graphics and color based on my logo

```html
<!DOCTYPE html>
<html lang="en">
<head>
<meta charset="utf-8">
<title>Holistic and Sports Psychology Consulting Flyer</title>
<link rel="stylesheet" href="https://fonts.googleapis.com/css2?family=Delius&family=Montserrat:wght@500;600;700;800&display=swap">
<style>
  :root {
    --purple: #5244a0;
    --purple-light: #6a58ad;
    --purple-dark: #4a3c98;
    --green: #a6d06d;
    --teal: #5a8f92;
    --sage: #86b285;
    --navy: #2c4f8b;
    --panel: #e6e7e9;
    --ink: #2a2a2a;
    --white: #ffffff;
  }
  * { box-sizing: border-box; margin: 0; padding: 0; }
  html, body { width: 956px; height: 1200px; overflow: hidden; background: var(--white); }
  .flyer { position: relative; width: 956px; height: 1200px; overflow: hidden; background: var(--white); font-family: "Montserrat", sans-serif; color: var(--ink); }
  .abs { position: absolute; }

  .brand-mark { left: 47px; top: 58px; width: 102px; height: 102px; border-radius: 50%; border: 4px solid var(--purple-dark); background: var(--white); }
  .brand-bar { left: 149px; top: 117px; width: 319px; height: 22px; background: var(--green); }
  .brand-name { left: 162px; top: 84px; font-family: "Delius", cursive; font-size: 26px; color: var(--purple-dark); letter-spacing: 0.5px; white-space: nowrap; }

  .hero-band { left: 0; top: 182px; width: 720px; height: 228px; background: linear-gradient(90deg, var(--purple-light), var(--purple-dark)); }
  .hero-title { left: 47px; top: 200px; font-family: "Delius", cursive; font-size: 44px; line-height: 48px; font-weight: 400; }
  .hero-title .lead { color: var(--white); display: block; }
  .hero-title .accent { color: var(--green); display: block; }

  .hero-art { left: 0; top: 0; width: 956px; height: 500px; }

  .section-heading { left: 47px; top: 430px; font-weight: 800; font-size: 25px; line-height: 29px; color: var(--navy); letter-spacing: 0.2px; }

  .services { left: 0; top: 512px; width: 956px; height: 262px; background: var(--panel); }
  .service { position: absolute; }
  .service.left { width: 520px; }
  .service.right { width: 360px; }
  .service-icon { position: absolute; left: 0; top: 0; width: 38px; height: 38px; }
  .service-title { position: absolute; left: 47px; top: 7px; font-weight: 700; font-size: 18px; color: var(--purple-dark); white-space: nowrap; }
  .service-title.navy { color: var(--navy); }
  .service-text { position: absolute; left: 4px; right: 0; top: 42px; font-size: 11.5px; line-height: 14.5px; font-weight: 500; color: var(--ink); }
  .service.left .service-text { white-space: nowrap; }

  .portrait { left: 25px; top: 803px; width: 250px; height: 250px; }

  .bio-name { left: 293px; top: 800px; font-family: "Delius", cursive; font-size: 40px; font-weight: 400; color: var(--purple-dark); white-space: nowrap; }
  .bio-text { left: 295px; top: 858px; width: 640px; font-family: "Delius", cursive; font-size: 13.6px; line-height: 18.5px; color: var(--ink); }
  .bio-text p + p { margin-top: 9px; }

  .info { font-size: 25px; color: var(--purple-dark); font-weight: 500; line-height: 32px; white-space: nowrap; }
  .info strong { font-weight: 700; display: flex; align-items: center; gap: 4px; }
  .info-telehealth { left: 284px; top: 1000px; }
  .info-sessions { left: 656px; top: 1002px; }

  .footer { left: 0; top: 1111px; width: 956px; height: 89px; }
  .footer-phone { left: 45px; top: 1139px; display: flex; align-items: center; gap: 10px; color: var(--white); font-weight: 700; font-size: 25px; }
  .footer-address { left: 405px; top: 1134px; display: flex; align-items: center; gap: 10px; color: var(--white); font-weight: 500; font-size: 14.5px; line-height: 19px; }
  .footer-web { left: 676px; top: 1143px; display: flex; align-items: center; gap: 12px; color: var(--white); font-weight: 500; font-size: 14.5px; }
</style>
</head>
<body>
<div class="flyer">

  <div class="abs brand-mark"></div>
  <div class="abs brand-bar"></div>
  <div class="abs brand-name">Dr. Elise Navarro-Hart</div>

  <div class="abs hero-band"></div>

  <svg class="abs hero-art" viewBox="0 0 956 500">
    <defs>
      <linearGradient id="leafGlow" x1="0" y1="0" x2="1" y2="1">
        <stop offset="0" stop-color="#7fa35a"/>
        <stop offset="0.5" stop-color="#b9c98e"/>
        <stop offset="1" stop-color="#5f7f40"/>
      </linearGradient>
    </defs>
    <circle cx="745" cy="240" r="246" fill="var(--green)"/>
    <circle cx="729" cy="218" r="234" fill="var(--white)"/>
    <circle cx="729" cy="218" r="225" fill="url(#leafGlow)" role="img" aria-label="Photo of cheering young soccer players outdoors, one holding a ball overhead"/>
  </svg>

  <h1 class="abs hero-title">
    <span class="lead">Holistic Psychology</span>
    <span class="accent">and Sports Psychology</span>
    <span class="accent">Consulting</span>
  </h1>

  <h2 class="abs section-heading">WAYS TO IMPROVE ATHLETIC PERFORMANCE<br>USING SPORTS AND HOLISTIC PSYCHOLOGY</h2>

  <section class="abs services">
    <div class="service left" style="left:43px; top:12px;">
      <svg class="service-icon" viewBox="0 0 38 38"><circle cx="19" cy="19" r="18" fill="var(--green)"/><circle cx="19" cy="18" r="15.5" fill="var(--purple-dark)"/><circle cx="19" cy="14" r="5" fill="none" stroke="#fff" stroke-width="1.8"/><path d="M10 25 q5 -3 9 0 h6" fill="none" stroke="#fff" stroke-width="1.8" stroke-linecap="round"/></svg>
      <div class="service-title navy">Mental Skills Training</div>
      <p class="service-text">Ex: visualization, goal-setting, motivation, self- talk,<br>mindset, concentration techniques</p>
    </div>
    <div class="service left" style="left:43px; top:92px;">
      <svg class="service-icon" viewBox="0 0 38 38"><circle cx="19" cy="19" r="18" fill="var(--green)"/><circle cx="19" cy="18" r="15.5" fill="var(--purple-dark)"/><g fill="#fff"><rect x="11" y="19" width="3" height="7"/><rect x="16" y="16" width="3" height="10"/><rect x="21" y="13" width="3" height="13"/><rect x="26" y="10" width="3" height="16"/></g></svg>
      <div class="service-title">Performance Enhancement</div>
      <p class="service-text">Eliminate psychological barriers that are hindering performance<br>such as self- doubt, perfectionism, fear of failure, and burnout</p>
    </div>
    <div class="service left" style="left:43px; top:172px;">
      <svg class="service-icon" viewBox="0 0 38 38"><circle cx="19" cy="19" r="18" fill="var(--green)"/><circle cx="19" cy="18" r="15.5" fill="var(--purple-dark)"/><path d="M13 27 v-5 a7 7 0 1 1 10 -6 l2 4 h-2 v3 h-3 v4" fill="none" stroke="#fff" stroke-width="1.8" stroke-linejoin="round"/></svg>
      <div class="service-title navy">Mental Health</div>
      <p class="service-text">Anxiety and stress management by using things such as relaxation<br>techniques, breathwork, and mindfulness practices</p>
    </div>

    <div class="service right" style="left:590px; top:18px;">
      <svg class="service-icon" viewBox="0 0 38 38"><circle cx="19" cy="19" r="18" fill="var(--green)"/><circle cx="19" cy="18" r="15.5" fill="var(--purple-dark)"/><path d="M12 10 h6 v10 l6 4 v3 h-12 z" fill="#fff"/><path d="M23 9 l5 2 v4 q0 4 -5 6 q-5 -2 -5 -6 v-4 z" fill="none" stroke="#fff" stroke-width="1.5"/></svg>
      <div class="service-title">Injury Recovery Support</div>
      <p class="service-text">Assist athletes in maintain resilience and positive mental attitude during rehabilitation as well as processing emotions relating to any potential trauma caused by the injury or life transitions resulting from it.</p>
    </div>
    <div class="service right" style="left:590px; top:146px;">
      <svg class="service-icon" viewBox="0 0 38 38"><circle cx="19" cy="19" r="18" fill="var(--green)"/><circle cx="19" cy="18" r="15.5" fill="var(--purple-dark)"/><g fill="none" stroke="#fff" stroke-width="1.6" stroke-linecap="round"><path d="M19 9 v16 M14 27 h10 M11 13 h16"/><path d="M11 13 l-3 7 h6 z M27 13 l-3 7 h6 z"/></g></svg>
      <div class="service-title navy">Burnout prevention</div>
      <p class="service-text">Teach athletes how to have balance in sports and life so they can experience longevity in their sports as well as overall optimal health and well-being.</p>
    </div>
  </section>

  <svg class="abs portrait" viewBox="0 0 250 250">
    <defs>
      <linearGradient id="ringTone" x1="0" y1="0" x2="1" y2="1">
        <stop offset="0" stop-color="var(--teal)"/>
        <stop offset="1" stop-color="var(--sage)"/>
      </linearGradient>
      <linearGradient id="beachTone" x1="0" y1="0" x2="0" y2="1">
        <stop offset="0" stop-color="#b9c6cf"/>
        <stop offset="1" stop-color="#8a98aa"/>
      </linearGradient>
    </defs>
    <circle cx="125" cy="125" r="124" fill="url(#ringTone)"/>
    <circle cx="125" cy="125" r="118" fill="var(--white)"/>
    <circle cx="125" cy="125" r="112" fill="url(#beachTone)" role="img" aria-label="Portrait photo of the psychologist seated on a sandy beach"/>
  </svg>

  <h2 class="abs bio-name">Dr. Elise Navarro-Hart</h2>
  <div class="abs bio-text">
    <p>Dr. Elise Navarro-Hart is a licensed psychologist. She understands the unique expe-<br>riences of athletes due to her background as an All American swimmer, collegiate and<br>age group swim coach, parent of a collegiate/professional athlete, and sports psychology<br>researcher. She works with athletes to optimize performance and overall well-being.</p>
    <p>Her specializations include: performance anxiety, mental performance, stress management,<br>anxiety, depressions, trauma, life transitions, relationship issues, injury, and sleep.</p>
  </div>

  <div class="abs info info-telehealth">
    All services are provided
    <strong><svg width="30" height="30" viewBox="0 0 30 30"><rect x="3" y="2" width="16" height="26" rx="3" fill="none" stroke="var(--purple-dark)" stroke-width="2"/><circle cx="11" cy="13" r="3" fill="var(--purple-dark)"/><path d="M6 23 q5 -6 10 0" fill="var(--purple-dark)"/><rect x="17" y="5" width="11" height="7" rx="1.5" fill="var(--purple-dark)"/></svg>online via telehealth</strong>
  </div>
  <div class="abs info info-sessions">
    Sessions are
    <strong><svg width="30" height="30" viewBox="0 0 30 30"><circle cx="15" cy="17" r="11" fill="none" stroke="var(--purple-dark)" stroke-width="2.4"/><path d="M12 3 h6 M15 3 v3 M15 17 v-6 M15 17 l4 3" stroke="var(--purple-dark)" stroke-width="2.4" stroke-linecap="round" fill="none"/></svg>30 or 55 minutes</strong>
  </div>

  <svg class="abs footer" viewBox="0 0 956 89" aria-hidden="true">
    <defs>
      <linearGradient id="footerTone" x1="0" y1="0" x2="1" y2="0">
        <stop offset="0" stop-color="var(--teal)"/>
        <stop offset="1" stop-color="var(--sage)"/>
      </linearGradient>
    </defs>
    <rect x="0" y="0" width="956" height="89" fill="url(#footerTone)"/>
    <path d="M0 0 H338 Q352 0 360 14 L397 89 H0 Z" fill="var(--purple)"/>
    <path d="M338 0 Q352 0 360 14 L397 89" fill="none" stroke="var(--white)" stroke-width="2"/>
  </svg>

  <div class="abs footer-phone">
    <svg width="30" height="30" viewBox="0 0 30 30"><circle cx="15" cy="15" r="14" fill="var(--white)"/><path d="M10 8 l3 0 l1.5 4 l-2 1.5 q1.5 3 4 4 l1.5 -2 l4 1.5 v3 q-1 2 -3 2 q-6 -1 -10 -8 q-1 -3 1 -6z" fill="var(--purple)"/></svg>
    555-014-2290
  </div>
  <div class="abs footer-address">
    <svg width="30" height="30" viewBox="0 0 30 30"><circle cx="15" cy="15" r="14" fill="var(--white)"/><path d="M15 7 a6 6 0 0 1 6 6 q0 4 -6 10 q-6 -6 -6 -10 a6 6 0 0 1 6 -6z" fill="var(--teal)"/><circle cx="15" cy="13" r="2.3" fill="var(--white)"/></svg>
    <span>2280 Harbor Glen Road #310<br>Seaview Bay, FL 32000</span>
  </div>
  <div class="abs footer-web">
    <svg width="30" height="30" viewBox="0 0 30 30"><circle cx="15" cy="15" r="14" fill="var(--white)"/><g fill="none" stroke="var(--purple)" stroke-width="1.5"><circle cx="15" cy="15" r="8"/><ellipse cx="15" cy="15" rx="3.5" ry="8"/><path d="M7 15 h16 M8.5 11 h13 M8.5 19 h13"/></g></svg>
    www.drelisenavarro.com
  </div>

</div>
</body>
</html>
```